Event flyer for Sunday night Youth Group

Need a 4 x 6 or 5 x 7 flyer for a new youth group starting on April 14. The youth group is for students in middle school and high school so it needs to look fun and cool, but not childish. I prefer it not to include pictures of people unless it's so obscure you can't really see their faces. I've uploaded some pictures of flyers I like. I've also attached a couple versions of our logo to use on the flyer.
Information the flyer needs to include:
Youth Group
Sundays, 6-8pm (beginning April 14)
Location: Wexlander's - 4182 Quillon Ridge Ave N, Marlowe, 97158
There will be dinner, games, friends, and a message.
Target Market(s)
Youth ages 13-18
Industry/Entity Type
Church
Colors
Look and feel

```html
<!DOCTYPE html>
<html lang="en">
<head>
<meta charset="utf-8">
<title>Youth Group – Sundays 6–8pm</title>
<link rel="stylesheet" href="https://fonts.googleapis.com/css2?family=Bebas+Neue&family=Poppins:wght@500;600;700&display=swap">
<style>
  :root {
    --ink: #25465a;
    --sage: #96ab8b;
    --ring: #80957f;
    --mist: #b9bcc2;
    --white: #ffffff;
    --soft-white: #eef0ee;
    --bg-warm: #8a9580;
    --bg-mid: #6a9a8a;
    --bg-teal: #22998f;
    --dash: #5aa9d6;
  }
  html, body {
    margin: 0;
    padding: 0;
    width: 857px;
    height: 1200px;
    overflow: hidden;
  }
  .flyer {
    position: relative;
    width: 857px;
    height: 1200px;
    overflow: hidden;
    font-family: "Poppins", sans-serif;
    color: var(--white);
  }
  .backdrop {
    position: absolute;
    inset: 0;
    background:
      radial-gradient(ellipse 420px 300px at 95% 5%, var(--bg-teal) 0%, transparent 75%),
      radial-gradient(ellipse 360px 260px at 10% 80%, var(--bg-mid) 0%, transparent 80%),
      linear-gradient(160deg, var(--bg-warm) 0%, var(--bg-mid) 45%, var(--bg-warm) 100%);
  }
  .artwork {
    position: absolute;
    inset: 0;
  }
  .brand {
    position: absolute;
    top: 220px;
    left: 0;
    width: 857px;
    text-align: center;
    font-weight: 500;
    color: var(--white);
    line-height: 1;
  }
  .brand-name {
    display: block;
    font-size: 30px;
    letter-spacing: 2px;
    padding-left: 2px;
  }
  .brand-sub {
    display: block;
    margin-top: 4px;
    font-size: 14px;
    letter-spacing: 9px;
    padding-left: 9px;
  }
  .details {
    position: absolute;
    top: 1010px;
    left: 0;
    width: 857px;
    margin: 0;
    text-align: center;
  }
  .details-lead {
    display: block;
    font-weight: 700;
    font-size: 15px;
    color: var(--soft-white);
    letter-spacing: 0.2px;
  }
  .details-list {
    display: block;
    margin-top: 0;
    font-weight: 600;
    font-size: 22px;
    color: var(--soft-white);
  }
</style>
</head>
<body>
<main class="flyer">
  <div class="backdrop" role="img" aria-label="Abstract flowing teal and sage paint shapes"></div>

  <svg class="artwork" width="857" height="1200" viewBox="0 0 857 1200" xmlns="http://www.w3.org/2000/svg">
    <g class="emblem-disc">
      <circle cx="424" cy="589" r="303" fill="var(--ring)"/>
      <circle cx="424" cy="589" r="290" fill="var(--ink)"/>
      <g fill="none" stroke="var(--dash)" stroke-width="1.2" stroke-dasharray="12 8">
        <circle cx="424" cy="589" r="266"/>
        <circle cx="424" cy="589" r="251"/>
        <circle cx="424" cy="589" r="235"/>
        <circle cx="424" cy="589" r="220"/>
      </g>
    </g>

    <text class="title-youth" x="424" y="597" text-anchor="middle" font-family="Bebas Neue, sans-serif" font-size="146" fill="var(--sage)">YOUTH</text>
    <text class="title-group" x="424" y="665" text-anchor="middle" font-family="Bebas Neue, sans-serif" font-size="70" fill="var(--mist)">GROUP</text>
    <text class="schedule" x="288" y="777" font-family="Bebas Neue, sans-serif" font-size="46" fill="var(--white)" textLength="272" lengthAdjust="spacingAndGlyphs">SUNDAYS, 6-8PM</text>
    <text class="schedule-start" x="424" y="806" text-anchor="middle" font-family="Poppins, sans-serif" font-weight="600" font-size="21" fill="var(--white)">beginning April 14</text>

    <g class="location-band">
      <rect x="83" y="917" width="688" height="58" rx="29" fill="var(--ink)"/>
      <text x="100" y="960" font-family="Bebas Neue, sans-serif" font-size="41" fill="var(--white)" textLength="637" lengthAdjust="spacingAndGlyphs">WEXLANDER'S - 4182 QUILLON RIDGE AVE N, MARLOWE, 97158</text>
    </g>
  </svg>

  <div class="brand">
    <span class="brand-name">HOLLOWAY</span>
    <span class="brand-sub">FELLOWSHIP</span>
  </div>

  <p class="details">
    <span class="details-lead">THERE WILL BE</span>
    <span class="details-list">dinner, games, friends, and a message</span>
  </p>
</main>
</body>
</html>
```